"Harrow Crest Builders" is a residential building company and needs a new business card design and may re

We would like a redesign based on the existing logo, and would like to see a new font as well. We are bespoke home builders who build sustainable energy efficient homes.

Industry/Entity Type

Construction

Contact Information for Business Card

Business card size 40mm x 90mm

Colors

Designer to choose colors to be used in the design.

```html
<!DOCTYPE html>
<html lang="en">
<head>
<meta charset="utf-8">
<title>Harrow Crest Builders — Business Card</title>
<link rel="stylesheet" href="https://fonts.googleapis.com/css2?family=Open+Sans:wght@400;600;700&family=Roboto+Condensed:wght@700&display=swap">
<style>
  :root {
    --backdrop: #2b2b2c;
    --card: #1f1f20;
    --card-edge: #2a2a2b;
    --lime: #b5d334;
    --white: #f4f4f4;
    --muted: #9a9a9a;
  }
  * { margin: 0; padding: 0; box-sizing: border-box; }
  html, body {
    width: 1200px;
    height: 900px;
    overflow: hidden;
    background: var(--backdrop);
    font-family: "Open Sans", Arial, sans-serif;
    color: var(--white);
  }
  .sheet {
    position: relative;
    width: 1200px;
    height: 900px;
  }
  .card {
    position: absolute;
    left: 220px;
    width: 760px;
    height: 338px;
    background: var(--card);
    border: 1px solid var(--card-edge);
    box-shadow: 0 10px 28px rgba(0,0,0,0.45);
  }
  .card--front { top: 80px; }
  .card--back { top: 470px; }

  /* Front */
  .brand {
    position: absolute;
    left: 0; right: 0;
    top: 110px;
    display: flex;
    justify-content: center;
    align-items: center;
    gap: 18px;
  }
  .brand__mark {
    width: 44px;
    height: 44px;
    background: var(--lime);
  }
  .brand__name {
    font-family: "Open Sans", Arial, sans-serif;
    font-weight: 600;
    font-size: 44px;
    letter-spacing: 0.5px;
    color: var(--white);
    line-height: 1;
  }
  .front-web {
    position: absolute;
    left: 0; right: 0;
    bottom: 58px;
    text-align: center;
    font-size: 15px;
    letter-spacing: 4px;
    color: var(--white);
  }
  .front-web__domain { color: var(--lime); }

  /* Back */
  .holder {
    position: absolute;
    left: 70px;
    top: 78px;
    font-family: "Roboto Condensed", "Arial Narrow", sans-serif;
    font-weight: 700;
    font-size: 36px;
    color: var(--lime);
    letter-spacing: 0.5px;
    line-height: 1;
    padding-top: 12px;
  }
  .divider {
    position: absolute;
    left: 372px;
    top: 66px;
    width: 2px;
    height: 70px;
    background: var(--muted);
  }
  .contacts {
    position: absolute;
    left: 398px;
    top: 68px;
    list-style: none;
    font-size: 17px;
    line-height: 22px;
  }
  .contacts__item {
    display: flex;
    align-items: center;
    gap: 10px;
  }
  .contacts__icon {
    width: 16px;
    height: 16px;
    flex: none;
  }
  .company {
    position: absolute;
    left: 0; right: 0;
    top: 200px;
    text-align: center;
    font-size: 17px;
    line-height: 23px;
  }
  .company__name { font-weight: 700; }
</style>
</head>
<body>
<main class="sheet">
  <section class="card card--front" aria-label="Business card front">
    <div class="brand">
      <span class="brand__mark" aria-hidden="true"></span>
      <span class="brand__name">harrow crest builders</span>
    </div>
    <p class="front-web">www.<span class="front-web__domain">harrowcrestbuilders</span>.com.au</p>
  </section>

  <section class="card card--back" aria-label="Business card back">
    <h1 class="holder">DANIEL FERRANTE</h1>
    <span class="divider" aria-hidden="true"></span>
    <ul class="contacts">
      <li class="contacts__item">
        <svg class="contacts__icon" viewBox="0 0 16 16" aria-hidden="true">
          <rect x="4" y="1" width="8" height="14" rx="1.5" fill="none" stroke="var(--lime)" stroke-width="1.6"/>
          <rect x="5.5" y="3" width="5" height="8" fill="var(--lime)"/>
        </svg>
        <span>0400 555 318</span>
      </li>
      <li class="contacts__item">
        <svg class="contacts__icon" viewBox="0 0 16 16" aria-hidden="true">
          <rect x="1" y="3.5" width="14" height="9.5" fill="var(--lime)"/>
          <path d="M1 3.5 L8 9 L15 3.5" fill="none" stroke="var(--card)" stroke-width="1.3"/>
        </svg>
        <span>daniel@harrowcrestbuilders.com.au</span>
      </li>
      <li class="contacts__item">
        <svg class="contacts__icon" viewBox="0 0 16 16" aria-hidden="true">
          <circle cx="8" cy="8" r="6.5" fill="var(--lime)"/>
          <path d="M1.5 8 H14.5 M8 1.5 C5 5 5 11 8 14.5 M8 1.5 C11 5 11 11 8 14.5" fill="none" stroke="var(--card)" stroke-width="1"/>
        </svg>
        <span>www.harrowcrestbuilders.com.au</span>
      </li>
    </ul>
    <address class="company" style="font-style: normal;">
      <div class="company__name">Harrow Crest Builders Pty Ltd</div>
      <div>PO Box 4820 Parkside, LPO Northvale WA 6003</div>
      <div>Registration 40817 | ABN: 52 604 318 297</div>
    </address>
  </section>
</main>
</body>
</html>
```